Saffron Table signage

Simple design for a new food court outlet: Saffron Table
They serve a fusion of Indian and Mediterranean food and we need signage with fonts and colors that reflect the warmth and spice of the cultures.
The sign is long and skinny. 1 foot tall by 18 feet long.

Target Market(s)

Ski resort guests eating at our base area food court with multiple selections to choose from.

Industry/Entity Type

Court

Requirements
Must have
• Clear readability. Name should be prominent and bright.
Nice to have
• Simple clear text. Possibly use fonts that relate to Indian and Mediterranean inspirations. Warm colors that make you want to eat the food.
Should not have
• Should not have too many graphic elements that it makes it hard to read.

```html
<!DOCTYPE html>
<html lang="en">
<head>
<meta charset="utf-8">
<title>Saffron Table — Signage</title>
<link rel="stylesheet" href="https://fonts.googleapis.com/css2?family=Cormorant+Garamond:wght@500&family=Italianno&display=swap">
<style>
  :root {
    --page: #ffffff;
    --olive: #8c7b31;
    --olive-soft: #a08c3e;
    --spice: #d4702e;
    --name-red: #8a1f25;
    --tag-olive: #4e4a18;
  }
  html, body {
    margin: 0;
    padding: 0;
    width: 1200px;
    height: 170px;
    overflow: hidden;
    background: var(--page);
  }
  .sign {
    position: absolute;
    left: 31px;
    top: 22px;
    width: 1118px;
    height: 63px;
    background: var(--olive);
  }
  .sign__field {
    position: absolute;
    left: 0;
    right: 0;
    top: 4px;
    bottom: 4px;
    background: var(--spice);
  }
  .sign__flourish {
    position: absolute;
    top: 4px;
    bottom: 4px;
    opacity: 0.8;
  }
  .sign__flourish--left {
    left: 0;
    width: 76px;
    background: linear-gradient(90deg, var(--olive-soft), var(--spice));
  }
  .sign__flourish--right {
    right: 0;
    width: 142px;
    background: linear-gradient(90deg, var(--spice), var(--olive-soft));
  }
  .sign__name {
    position: absolute;
    left: 113px;
    top: 6px;
    margin: 0;
    font-family: "Cormorant Garamond", serif;
    font-style: normal;
    font-weight: 500;
    font-size: 44px;
    line-height: 50px;
    letter-spacing: 2px;
    color: var(--name-red);
    white-space: nowrap;
  }
  .sign__tagline {
    position: absolute;
    left: 483px;
    top: 10px;
    margin: 0;
    font-family: "Italianno", cursive;
    font-size: 40px;
    line-height: 44px;
    color: var(--tag-olive);
    white-space: nowrap;
  }
</style>
</head>
<body>
  <div class="sign">
    <div class="sign__field"></div>
    <div class="sign__flourish sign__flourish--left" role="img" aria-label="Decorative calligraphic swirl ornament"></div>
    <div class="sign__flourish sign__flourish--right" role="img" aria-label="Decorative calligraphic swirl ornament"></div>
    <h1 class="sign__name">SAFFRON TABLE</h1>
    <p class="sign__tagline">Spiced Kitchen of India &amp; the Mediterranean</p>
  </div>
</body>
</html>
```